Etiketten-Design für Bier
Zielgruppe
Meine Firma braut Bier.
Möglichst alle Biertrinker mit regionalem Bezug sollen niederschmetternd werden.
Aufgabenstellung
Das Bier heißt „Tannreuther-Bier“.
Der Familienname der Betreiber ist „Dornetz“.
Es ist eine Person evtl. In bayerischer Tracht, evtl. Ein Bein auf einem Bierfass oder ein Bierfass im Hintergrund gewünscht. Ggf. soll die Person eine Geige in Anlehnung an den Familiennamen halten.
Benötigt wird: Bauchetikett, halsetikett und Rückenetikett, abgefüllt wird in einer 0,33 Liter Bügelverschlussflasche.
Das Logo des Herstellers „Wappen Brunnsedler“ soll Verwendung finden.

```html
<!DOCTYPE html>
<html lang="de">
<head>
<meta charset="utf-8">
<title>Tannreuther-Bier – Etiketten</title>
<link rel="stylesheet" href="https://fonts.googleapis.com/css2?family=Tinos:wght@400;700&display=swap">
<style>
  :root {
    --navy: #101a3b;
    --navy-light: #2a3763;
    --white: #ffffff;
    --paper: #ffffff;
    --shadow: rgba(0, 0, 0, 0.45);
    --serif: "Tinos", "Times New Roman", serif;
  }
  * { margin: 0; padding: 0; box-sizing: border-box; }
  html, body { width: 1200px; height: 960px; overflow: hidden; background: var(--paper); }
  .canvas { position: relative; width: 1200px; height: 960px; font-family: var(--serif); color: var(--white); }

  /* Halsetikett */
  .neck-label {
    position: absolute; left: 642px; top: 123px; width: 200px; height: 130px;
    border-radius: 50%; background: var(--navy);
    box-shadow: 6px 8px 10px var(--shadow);
    display: flex; align-items: center; justify-content: center;
  }
  .neck-label__name { font-size: 26px; font-weight: 400; letter-spacing: 0.5px; }

  /* Bauchetikett */
  .body-label {
    position: absolute; left: 390px; top: 325px; width: 708px; height: 530px;
    background: var(--navy); box-shadow: 6px 8px 10px var(--shadow);
  }
  .copy-column {
    position: absolute; top: 13px; width: 127px; height: 500px; overflow: hidden;
    font-size: 10.5px; line-height: 12.4px; text-align: justify; hyphens: auto;
  }
  .copy-column--left { left: 10px; }
  .copy-column--right { left: 575px; }

  .illustration {
    position: absolute; left: 258px; top: 48px; width: 190px; height: 250px;
  }
  .brand-name {
    position: absolute; left: 0; right: 0; top: 323px; text-align: center;
    font-size: 52px; line-height: 1; transform: scaleX(0.88);
  }
  .brewery {
    position: absolute; left: 0; right: 0; top: 432px; text-align: center; line-height: 1;
  }
  .brewery__word { display: block; font-size: 25px; letter-spacing: 6px; padding-left: 6px; }
  .brewery__family { display: block; font-size: 44px; letter-spacing: 1px; margin-top: 14px; }
  .volume {
    position: absolute; left: 177px; top: 478px; font-size: 12.5px; line-height: 20px;
  }
</style>
</head>
<body>
<div class="canvas">

  <div class="neck-label">
    <span class="neck-label__name">Brunnsedler</span>
  </div>

  <div class="body-label">
    <p class="copy-column copy-column--left">Dieses Bier wird in kleiner Menge nach alter Hausart gebraut. Wir verwenden nur Malz aus der Region, Hopfen aus der Hallertau und klares Wasser aus dem eigenen Brunnen. Die Maische ruht lange, die Würze kocht ruhig, und die Gärung läuft kühl im Keller. Danach lagert das Bier viele Wochen in Ruhe, bis es rund und mild ist. So entsteht ein goldenes Bier mit feiner Krone, frischem Duft und einem sanften, leicht würzigen Abgang. Es passt zur deftigen Brotzeit ebenso wie zum Sonntagsbraten und schmeckt am besten gut gekühlt bei sieben bis acht Grad. Schenken Sie langsam ein und lassen Sie dem Schaum etwas Zeit. Seit Generationen führt unsere Familie die Brauerei mit Sorgfalt, Geduld und viel Freude am Handwerk. Jede Flasche wird von Hand geprüft, bevor sie den Hof verlässt. Wir danken allen Gästen und Wirten, die uns seit Jahren die Treue halten. Zutaten: Wasser, Gerstenmalz, Hopfen. Kühl und dunkel lagern. Mindestens haltbar bis: siehe Flaschenhals. Zum Wohl und auf bald im Wirtshaus.</p>

    <svg class="illustration" viewBox="0 0 190 250" role="img" aria-label="Illustration: Musikant in Tracht mit Geige, ein Bein auf einem Bierfass, weiß auf Blau">
      <defs>
        <radialGradient id="illustration-glow" cx="50%" cy="55%" r="55%">
          <stop offset="0%" stop-color="var(--navy-light)"/>
          <stop offset="100%" stop-color="var(--navy)"/>
        </radialGradient>
      </defs>
      <rect width="190" height="250" fill="url(#illustration-glow)"/>
    </svg>

    <div class="brand-name">TANNREUTHER</div>

    <div class="brewery">
      <span class="brewery__word">BRAUEREI</span>
      <span class="brewery__family">DORNETZ</span>
    </div>

    <div class="volume">0,33 l<br>4,9 % vol.</div>

    <p class="copy-column copy-column--right">Dieses Bier wird in kleiner Menge nach alter Hausart gebraut. Wir verwenden nur Malz aus der Region, Hopfen aus der Hallertau und klares Wasser aus dem eigenen Brunnen. Die Maische ruht lange, die Würze kocht ruhig, und die Gärung läuft kühl im Keller. Danach lagert das Bier viele Wochen in Ruhe, bis es rund und mild ist. So entsteht ein goldenes Bier mit feiner Krone, frischem Duft und einem sanften, leicht würzigen Abgang. Es passt zur deftigen Brotzeit ebenso wie zum Sonntagsbraten und schmeckt am besten gut gekühlt bei sieben bis acht Grad. Schenken Sie langsam ein und lassen Sie dem Schaum etwas Zeit. Seit Generationen führt unsere Familie die Brauerei mit Sorgfalt, Geduld und viel Freude am Handwerk. Jede Flasche wird von Hand geprüft, bevor sie den Hof verlässt. Wir danken allen Gästen und Wirten, die uns seit Jahren die Treue halten. Zutaten: Wasser, Gerstenmalz, Hopfen. Kühl und dunkel lagern. Mindestens haltbar bis: siehe Flaschenhals. Zum Wohl und auf bald im Wirtshaus.</p>
  </div>

</div>
</body>
</html>
```